Vex Pim ORA Need a custom graphic

I need to have the attached chart re-designed in a hand colored pencil format. The heading needs to be changed to "The most effective methods for hiring sales people". Do not include the background logo in the sample file.

Place the attached Vex Pim ORA logo next to the most effective methods (91%)

```html
<!DOCTYPE html>
<html lang="en">
<head>
<meta charset="utf-8">
<title>The most effective methods for hiring sales people</title>
<link rel="stylesheet" href="https://fonts.googleapis.com/css2?family=Architects+Daughter&family=Indie+Flower&family=Gochi+Hand&family=Quicksand:wght@500&display=swap">
<style>
  :root {
    --paper: #ffffff;
    --ink: #1f3640;
    --grid: #4a5a60;
    --plot-red: #e0442e;
    --tick-red: #e2304c;
    --label-fill: #8ed4e8;
    --label-sheen: #c4ecf6;
    --label-edge: #1f3640;
    --title-text: #f4f7f7;
    --brand-blue: #1f4f9c;
  }
  html, body {
    margin: 0;
    padding: 0;
    width: 1200px;
    height: 808px;
    overflow: hidden;
    background: var(--paper);
  }
  .chart { display: block; width: 1200px; height: 808px; }
  .chart-title { font-family: "Gochi Hand", cursive; font-size: 31px; fill: var(--title-text); }
  .title-band { fill: var(--ink); }
  .axis-line { stroke: var(--ink); stroke-width: 5; stroke-linecap: round; fill: none; }
  .grid-line { stroke: var(--grid); stroke-width: 1; stroke-dasharray: 5 5; fill: none; }
  .tick-label { font-family: "Indie Flower", cursive; font-size: 18px; fill: var(--tick-red); }
  .axis-title { font-family: "Gochi Hand", cursive; font-size: 44px; fill: var(--ink); }
  .trend-line { stroke: var(--plot-red); stroke-width: 2.5; fill: none; stroke-linejoin: round; }
  .data-point { fill: var(--plot-red); }
  .method-box { fill: var(--label-fill); stroke: var(--label-edge); stroke-width: 2.5; }
  .method-sheen { fill: var(--label-sheen); opacity: .7; }
  .method-text { font-family: "Architects Daughter", cursive; font-size: 22px; fill: var(--ink); }
  .pointer { stroke: var(--plot-red); stroke-width: 2; fill: none; stroke-linecap: round; }
  .pointer-head { fill: var(--plot-red); }
  .brand-name { font-family: "Quicksand", sans-serif; font-weight: 500; font-size: 30px; fill: var(--brand-blue); }
  .brand-mark { fill: var(--brand-blue); }
</style>
</head>
<body>
<svg class="chart" viewBox="0 0 1100 745" preserveAspectRatio="none" xmlns="http://www.w3.org/2000/svg" role="img" aria-label="Line chart: predictive validity of hiring methods for sales people">
  <defs>
    <marker id="arrow-tip" viewBox="0 0 10 10" refX="8" refY="5" markerWidth="7" markerHeight="7" orient="auto">
      <path class="pointer-head" d="M0 0 L10 5 L0 10 L3 5 Z"/>
    </marker>
  </defs>

  <!-- title -->
  <path class="title-band" d="M250 14 Q620 6 988 12 Q994 40 990 66 Q620 72 246 66 Q240 40 250 14 Z"/>
  <text class="chart-title" x="617" y="49" text-anchor="middle" textLength="690" lengthAdjust="spacingAndGlyphs">The most effective methods for hiring sales people</text>

  <!-- grid -->
  <g class="grid">
    <line class="grid-line" x1="150" y1="112" x2="1075" y2="112"/>
    <line class="grid-line" x1="150" y1="175" x2="1075" y2="175"/>
    <line class="grid-line" x1="150" y1="238" x2="1075" y2="238"/>
    <line class="grid-line" x1="150" y1="301" x2="1075" y2="301"/>
    <line class="grid-line" x1="150" y1="364" x2="1075" y2="364"/>
    <line class="grid-line" x1="150" y1="427" x2="1075" y2="427"/>
    <line class="grid-line" x1="150" y1="490" x2="1075" y2="490"/>
    <line class="grid-line" x1="150" y1="552" x2="1075" y2="552"/>
    <line class="grid-line" x1="150" y1="615" x2="1075" y2="615"/>
    <line class="grid-line" x1="240" y1="40" x2="240" y2="685"/>
    <line class="grid-line" x1="320" y1="40" x2="320" y2="685"/>
    <line class="grid-line" x1="403" y1="40" x2="403" y2="685"/>
    <line class="grid-line" x1="485" y1="40" x2="485" y2="685"/>
    <line class="grid-line" x1="567" y1="40" x2="567" y2="685"/>
    <line class="grid-line" x1="650" y1="40" x2="650" y2="685"/>
    <line class="grid-line" x1="732" y1="40" x2="732" y2="685"/>
    <line class="grid-line" x1="815" y1="40" x2="815" y2="685"/>
    <line class="grid-line" x1="897" y1="40" x2="897" y2="685"/>
    <line class="grid-line" x1="980" y1="40" x2="980" y2="685"/>
    <line class="grid-line" x1="1060" y1="40" x2="1060" y2="685"/>
  </g>

  <!-- axes -->
  <path class="axis-line" d="M157 32 Q155 360 158 684"/>
  <path class="axis-line" d="M146 684 Q610 680 1076 683"/>

  <g class="tick-labels">
    <text class="tick-label" x="88" y="118">0.90</text>
    <text class="tick-label" x="88" y="181">0.80</text>
    <text class="tick-label" x="88" y="244">0.70</text>
    <text class="tick-label" x="88" y="307">0.60</text>
    <text class="tick-label" x="88" y="370">0.50</text>
    <text class="tick-label" x="88" y="433">0.40</text>
    <text class="tick-label" x="88" y="496">0.30</text>
    <text class="tick-label" x="88" y="558">0.20</text>
    <text class="tick-label" x="88" y="621">0.10</text>
    <text class="tick-label" x="88" y="686">0.00</text>
  </g>

  <text class="axis-title" transform="translate(72 362) rotate(-90)" text-anchor="middle">Predictive validity</text>
  <text class="axis-title" x="612" y="730" text-anchor="middle">hiring method</text>

  <!-- brand -->
  <rect class="brand-mark" x="262" y="139" width="18" height="18"/>
  <text class="brand-name" x="290" y="159">Vex Pim ORA</text>

  <!-- data -->
  <polyline class="trend-line" points="242,631 313,570 403,552 485,548 567,523 652,528 732,476 815,357 897,301 977,220 1057,128"/>
  <g class="points">
    <circle class="data-point" cx="242" cy="631" r="4.5"/>
    <circle class="data-point" cx="313" cy="570" r="4.5"/>
    <circle class="data-point" cx="403" cy="552" r="4.5"/>
    <circle class="data-point" cx="485" cy="548" r="4.5"/>
    <circle class="data-point" cx="567" cy="523" r="4.5"/>
    <circle class="data-point" cx="652" cy="528" r="4.5"/>
    <circle class="data-point" cx="732" cy="476" r="4.5"/>
    <circle class="data-point" cx="815" cy="357" r="4.5"/>
    <circle class="data-point" cx="897" cy="301" r="4.5"/>
    <circle class="data-point" cx="977" cy="220" r="4.5"/>
    <circle class="data-point" cx="1057" cy="128" r="4.5"/>
  </g>

  <!-- method labels -->
  <g class="method-label">
    <rect class="method-box" x="535" y="118" width="465" height="38" rx="3"/>
    <rect class="method-sheen" x="545" y="122" width="445" height="10"/>
    <text class="method-text" x="553" y="145" textLength="428" lengthAdjust="spacingAndGlyphs">Sales-specific multi-measurement Assessment, 91%</text>
    <path class="pointer" d="M1008 134 Q1024 128 1042 128" marker-end="url(#arrow-tip)"/>
  </g>
  <g class="method-label">
    <rect class="method-box" x="548" y="190" width="365" height="42" rx="3"/>
    <rect class="method-sheen" x="558" y="194" width="345" height="11"/>
    <text class="method-text" x="566" y="219" textLength="328" lengthAdjust="spacingAndGlyphs">Multi-measurement Assessment, 71%</text>
    <path class="pointer" d="M922 210 Q942 210 962 216" marker-end="url(#arrow-tip)"/>
  </g>
  <g class="method-label">
    <rect class="method-box" x="358" y="264" width="510" height="40" rx="3"/>
    <rect class="method-sheen" x="368" y="268" width="490" height="10"/>
    <text class="method-text" x="372" y="292" textLength="478" lengthAdjust="spacingAndGlyphs">Highly structured interview with scorecard, 57%</text>
    <path class="pointer" d="M846 283 Q866 286 884 292" marker-end="url(#arrow-tip)"/>
  </g>
  <g class="method-label">
    <rect class="method-box" x="428" y="320" width="328" height="40" rx="3"/>
    <rect class="method-sheen" x="438" y="324" width="308" height="10"/>
    <text class="method-text" x="442" y="348" textLength="298" lengthAdjust="spacingAndGlyphs">General mental ability, 51%</text>
    <path class="pointer" d="M764 342 Q784 344 801 352" marker-end="url(#arrow-tip)"/>
  </g>
  <g class="method-label">
    <rect class="method-box" x="490" y="402" width="255" height="36" rx="3"/>
    <rect class="method-sheen" x="500" y="406" width="235" height="9"/>
    <text class="method-text" x="500" y="428" textLength="236" lengthAdjust="spacingAndGlyphs">Reference check, 23%</text>
    <path class="pointer" d="M596 445 Q586 470 578 492" marker-end="url(#arrow-tip)"/>
  </g>
  <g class="method-label">
    <rect class="method-box" x="205" y="452" width="338" height="40" rx="3"/>
    <rect class="method-sheen" x="215" y="456" width="318" height="10"/>
    <text class="method-text" x="213" y="480" textLength="320" lengthAdjust="spacingAndGlyphs">Behavior/Personality test, 20%</text>
    <path class="pointer" d="M410 500 Q408 520 405 540" marker-end="url(#arrow-tip)"/>
  </g>
  <g class="method-label">
    <rect class="method-box" x="188" y="515" width="157" height="36" rx="3"/>
    <rect class="method-sheen" x="198" y="519" width="137" height="9"/>
    <text class="method-text" x="200" y="541" textLength="134" lengthAdjust="spacingAndGlyphs">Resume, 18%</text>
    <path class="pointer" d="M262 558 Q280 564 300 572" marker-end="url(#arrow-tip)"/>
  </g>
  <g class="method-label">
    <rect class="method-box" x="773" y="487" width="205" height="36" rx="3"/>
    <rect class="method-sheen" x="783" y="491" width="185" height="9"/>
    <text class="method-text" x="794" y="513" textLength="168" lengthAdjust="spacingAndGlyphs">skills test, 33%</text>
    <path class="pointer" d="M766 498 Q756 488 742 482" marker-end="url(#arrow-tip)"/>
  </g>
  <g class="method-label">
    <rect class="method-box" x="695" y="553" width="320" height="40" rx="3"/>
    <rect class="method-sheen" x="705" y="557" width="300" height="10"/>
    <text class="method-text" x="703" y="581" textLength="303" lengthAdjust="spacingAndGlyphs">Emotional intelligence, 23%</text>
    <path class="pointer" d="M688 555 Q674 546 662 536" marker-end="url(#arrow-tip)"/>
  </g>
  <g class="method-label">
    <rect class="method-box" x="362" y="585" width="306" height="38" rx="3"/>
    <rect class="method-sheen" x="372" y="589" width="286" height="9"/>
    <text class="method-text" x="372" y="612" textLength="286" lengthAdjust="spacingAndGlyphs">Traditional interview, 20%</text>
    <path class="pointer" d="M520 576 Q506 566 494 558" marker-end="url(#arrow-tip)"/>
  </g>
  <g class="method-label">
    <rect class="method-box" x="268" y="641" width="222" height="38" rx="3"/>
    <rect class="method-sheen" x="278" y="645" width="202" height="9"/>
    <text class="method-text" x="278" y="668" textLength="203" lengthAdjust="spacingAndGlyphs">Culture test, 13%</text>
    <path class="pointer" d="M266 660 Q254 652 246 642" marker-end="url(#arrow-tip)"/>
  </g>
</svg>
</body>
</html>
```